Need excellent graphic designer to build a template for company flyer.
Will involve rebranding existing flyer.

See KLT Consulting General Flyer for content. Also added Sales & Marketing as an example of our services.

Target Market(s)

Business owners and second tier management
Revenue: $10 million - $75 million (small companies), $76 million + (large companies)
Location: Southeast, Northeast
20+ employees

- Open to change processes, systems, structure, product/service offerings
- Committed to growth
- Committed to hiring people better than them

Industry/Entity Type

Graphic Designer

Font styles to use
Serif
Sans Serif

Requirements
Must have
• Logo
Open to new designs and professional styles that reflect a collaborative, credible and community-focused team - see website (www.kltcrew.com)
Tagline - "To advise and engineer success"
Easy to read and clear messaging
Should not have
• Stock images that are obvious, no handshake

```html
<!DOCTYPE html>
<html lang="en">
<head>
<meta charset="utf-8">
<title>KLT Consulting – Company Flyer</title>
<link rel="stylesheet" href="https://fonts.googleapis.com/css2?family=Fira+Sans:wght@400;600;700&family=Merriweather:wght@700&display=swap">
<style>
  :root {
    --navy: #0b3a94;
    --blue: #1763c8;
    --sky: #3aa0ec;
    --cyan: #2cc0f2;
    --cyan-light: #5fd2f7;
    --gold: #fcc419;
    --white: #ffffff;
    --red: #e3161d;
    --brand-ink: #0d4a86;
  }
  * { margin: 0; padding: 0; box-sizing: border-box; }
  html, body { width: 1200px; height: 927px; overflow: hidden; }
  body { font-family: "Fira Sans", Arial, sans-serif; color: var(--white); }

  .flyer {
    position: relative; width: 1200px; height: 927px; overflow: hidden;
    background: linear-gradient(135deg, var(--navy) 0%, var(--blue) 45%, var(--sky) 75%, var(--blue) 100%);
  }
  .flyer__waves { position: absolute; inset: 0; width: 1200px; height: 927px; }

  .brand-box {
    position: absolute; left: 40px; top: 55px; width: 340px; height: 147px;
    background: var(--cyan); color: var(--brand-ink);
  }
  .brand-box__lockup {
    position: absolute; left: 0; right: 0; top: 26px;
    display: flex; align-items: center; justify-content: center; gap: 14px;
  }
  .brand-box__dot { width: 34px; height: 34px; border-radius: 50%; background: var(--brand-ink); }
  .brand-box__name { font-weight: 700; font-size: 38px; line-height: 60px; }
  .brand-box__tagline {
    position: absolute; left: 0; right: 0; top: 112px; text-align: center;
    font-family: "Merriweather", Georgia, serif; font-weight: 700; font-size: 17.5px; line-height: 26px;
  }

  .brand-url {
    position: absolute; left: 40px; top: 208px; width: 340px; text-align: center;
    color: var(--red); font-weight: 700; font-size: 22px; line-height: 30px;
  }

  .block { position: absolute; white-space: nowrap; }
  .section-title { font-weight: 600; color: var(--gold); font-size: 25.5px; line-height: 30px; }
  .service-title { font-weight: 600; font-size: 20.5px; line-height: 24px; }
  .body-text { font-size: 17.6px; line-height: 21.9px; }
  .body-text strong { font-weight: 700; }

  .results-list { list-style: none; font-size: 17.6px; line-height: 24.6px; }
  .results-list li { position: relative; padding-left: 19px; }
  .results-list .tick { position: absolute; left: 0; top: 7px; width: 13px; height: 11px; }
  .results-list .wrap-out { margin-left: -19px; }

  .contact-band {
    position: absolute; left: 0; top: 827px; width: 1200px; height: 100px;
    background: linear-gradient(90deg, var(--cyan) 0%, var(--cyan-light) 50%, var(--cyan) 100%);
    color: var(--red); font-weight: 700;
  }
  .contact-band__address {
    position: absolute; left: 72px; top: 20px; font-size: 20px; line-height: 27px;
    font-variant: small-caps;
  }
  .contact-band__item { position: absolute; top: 32px; display: flex; align-items: center; gap: 22px; font-size: 20px; line-height: 26px; }
  .contact-band__item--phone { left: 495px; }
  .contact-band__item--web { left: 893px; gap: 12px; }
  .contact-band svg { width: 20px; height: 20px; }
</style>
</head>
<body>
<main class="flyer">
  <svg class="flyer__waves" viewBox="0 0 1200 927" aria-hidden="true">
    <path d="M0 420 C300 300 600 500 1200 250 L1200 0 L0 0 Z" fill="#0a3587" opacity=".35"/>
    <path d="M380 927 C600 650 900 520 1200 540 L1200 927 Z" fill="#5cb6f2" opacity=".35"/>
    <path d="M700 0 C820 180 1000 260 1200 230 L1200 0 Z" fill="#0c2f7a" opacity=".4"/>
    <path d="M560 927 C700 700 950 600 1200 620" stroke="#bfe4fb" stroke-width="3" fill="none" opacity=".45"/>
    <path d="M820 0 C900 160 1050 250 1200 260" stroke="#9fd4f7" stroke-width="2" fill="none" opacity=".4"/>
  </svg>

  <div class="brand-box">
    <div class="brand-box__lockup">
      <span class="brand-box__dot"></span>
      <span class="brand-box__name">KLT Consulting</span>
    </div>
    <p class="brand-box__tagline">To advise and engineer success</p>
  </div>
  <p class="brand-url">www.kltcrew.com</p>

  <h2 class="block section-title" style="left:28px;top:278px">ABOUT KLT CONSULTING</h2>
  <p class="block body-text" style="left:28px;top:315px">Founded in 2009, KLT’s mission is to align<br>with the strategic goals of business<br>partners to ensure objectivity,<br>accountability, execution and results. We<br>work with established companies from $10<br>million revenue or more, in all industries.</p>
  <h2 class="block section-title" style="left:28px;top:449px">Why KLT?</h2>
  <p class="block body-text" style="left:28px;top:477px">•<strong>Experienced</strong> - We have founded, owned,<br>operated, acquired and sold companies<br>from startup to above $500 million in<br>revenue to create significant shareholder<br>value. KLT was started to help business<br>owners by using our vast experience and<br>expertise.<br>•<strong>Diverse</strong> - As industry experts in many<br>business verticals, we bring a holistic<br>approach to solving business challenges<br>and accomplishing strategic goals. From<br>support personnel to senior partners, our<br>team has depth and knowledge in finance,<br>operations, sales, human resources and<br>technology.</p>

  <h2 class="block section-title" style="left:408px;top:52px">KLT’S CORE SERVICES INCLUDE</h2>
  <h3 class="block service-title" style="left:408px;top:89px">Business Advisory Services</h3>
  <p class="block body-text" style="left:408px;top:113px">We assist in the development and execution<br>of the company’s business goals and strategy<br>through understanding the entire business en-<br>vironment as well as personal goals to create a<br>comprehensive and realistic plan.</p>
  <h3 class="block service-title" style="left:408px;top:231px">Mergers &amp; Acquisition Services</h3>
  <p class="block body-text" style="left:408px;top:256px">Our team has experience in over 400 mergers<br>and acquisitions on both the buy and sell sides.<br>Services include incremental support for Due<br>Diligence, Research, Analysis, Exit Strategy,<br>Contract Negotiations and Post-Transaction<br>Integrations.</p>
  <h3 class="block service-title" style="left:408px;top:395px">Business Process Re-engineering</h3>
  <p class="block body-text" style="left:408px;top:419px">A full evaluation of your existing operational<br>processes and identification of methods with<br>complete documentation along with<br>recommendations to improve efficiencies and<br>performance.</p>

  <h3 class="block service-title" style="left:810px;top:51px">System Integrations</h3>
  <p class="block body-text" style="left:810px;top:75px">We specialize in financial, operating and<br>sales<br>system integrations involving strategy and<br>design, project management, training, docu-<br>mentation, quality control procedures and<br>communications.</p>
  <h3 class="block service-title" style="left:810px;top:215px">Financial Management</h3>
  <p class="block body-text" style="left:810px;top:239px">As CFOs, Controllers and Financial Analysts,<br>we align financial objectives with business<br>strategy, establish controls and can provide<br>outsourced services for you to effectively<br>manage your business.</p>
  <h3 class="block service-title" style="left:810px;top:357px">Sales and Marketing Solutions</h3>
  <p class="block body-text" style="left:810px;top:381px">We offer customized training and develop-<br>ment programs for your team to grow rev-<br>enue through sales and marketing. Sample<br>projects include branding, sales training,<br>process development, social media strategy<br>and website development.</p>

  <h2 class="block section-title" style="left:406px;top:545px">IN THE COMMUNITY</h2>
  <p class="block body-text" style="left:406px;top:573px">KLT is active in community and<br>professional organizations. We understand<br>the importance of helping people from all<br>walks of life have the opportunity to reach<br>their potential through business, non-<br>profit and professional development. Our<br>community involvement is at the core of<br>what we do, and we encourage our clients<br>to participate and contribute beyond their<br>business.</p>

  <h2 class="block section-title" style="left:812px;top:545px">CLIENT RESULTS</h2>
  <ul class="block results-list" style="left:812px;top:577px">
    <li><svg class="tick" viewBox="0 0 13 11"><path d="M1 6 L5 10 L12 1" stroke="#fff" stroke-width="1.6" fill="none"/></svg>Increased stakeholder value</li>
    <li><svg class="tick" viewBox="0 0 13 11"><path d="M1 6 L5 10 L12 1" stroke="#fff" stroke-width="1.6" fill="none"/></svg>Improved profitability</li>
    <li><svg class="tick" viewBox="0 0 13 11"><path d="M1 6 L5 10 L12 1" stroke="#fff" stroke-width="1.6" fill="none"/></svg>Performance and efficiency gains</li>
    <li><svg class="tick" viewBox="0 0 13 11"><path d="M1 6 L5 10 L12 1" stroke="#fff" stroke-width="1.6" fill="none"/></svg>Implemented management financial and<br>operational controls</li>
    <li><svg class="tick" viewBox="0 0 13 11"><path d="M1 6 L5 10 L12 1" stroke="#fff" stroke-width="1.6" fill="none"/></svg>Standardized and documented processes</li>
    <li><svg class="tick" viewBox="0 0 13 11"><path d="M1 6 L5 10 L12 1" stroke="#fff" stroke-width="1.6" fill="none"/></svg>Improved business processes</li>
    <li><svg class="tick" viewBox="0 0 13 11"><path d="M1 6 L5 10 L12 1" stroke="#fff" stroke-width="1.6" fill="none"/></svg>Improved quality and development of<br><span class="wrap-out">team</span></li>
    <li><svg class="tick" viewBox="0 0 13 11"><path d="M1 6 L5 10 L12 1" stroke="#fff" stroke-width="1.6" fill="none"/></svg>Secured new capital</li>
  </ul>

  <footer class="contact-band">
    <p class="contact-band__address">418 Lakeview Crossing Rd 310,<br>Maple Grove, FL 32810</p>
    <p class="contact-band__item contact-band__item--phone">
      <svg viewBox="0 0 20 20" aria-hidden="true"><path d="M2 7 C2 3 18 3 18 7 L15 9 L13 6 L7 6 L5 9 Z M5 10 L15 10 L17 17 L3 17 Z" fill="#e3161d"/></svg>
      407.555.0188
    </p>
    <p class="contact-band__item contact-band__item--web">
      <svg viewBox="0 0 20 20" aria-hidden="true"><g fill="none" stroke="#e3161d" stroke-width="1.6"><circle cx="10" cy="10" r="8"/><ellipse cx="10" cy="10" rx="3.5" ry="8"/><path d="M2 10 H18"/></g></svg>
      www.kltcrew.com
    </p>
  </footer>
</main>
</body>
</html>
```